Design the 21st Golden Reel Indie Screen Week Poster. Think modern, chic, cool, film, movies - driving people to the film festival - the film festivla is in San Francisco and the SF East Bay. Our logo is attached. Dates will be determined soon . please use - November 2 - 11, 2018 (for placement) Keep in mind abstract, chic, modern - eye catching. website is www.grisw.example

Target Market(s)

25 - 45 year old - upper middle class

Industry/Entity Type

Film Production

Colors

Designer to choose colors to be used in the design.

Requirements
Must have
• logo (attached) www.grisw.example - chic modern design
Nice to have
• best coolest poster ever!
Should not have
• CLIP ART!!!

```html
<!DOCTYPE html>
<html lang="en">
<head>
<meta charset="utf-8">
<title>21st Golden Reel Indie Screen Week</title>
<link rel="stylesheet" href="https://fonts.googleapis.com/css2?family=Amatic+SC:wght@700&family=Poiret+One&display=swap">
<style>
  :root {
    --ink: #0a0a0a;
    --paper: #ffffff;
    --red: #f2203c;
    --magenta: #b0479a;
    --violet: #6f4fb8;
    --periwinkle: #7a86c4;
    --blue: #3b2ca8;
    --night: #060606;
  }
  * { margin: 0; padding: 0; box-sizing: border-box; }
  html, body { width: 848px; height: 1200px; overflow: hidden; background: var(--night); }
  .poster { position: relative; width: 848px; height: 1200px; overflow: hidden; }
  .backdrop {
    position: absolute; inset: 0;
    background:
      linear-gradient(180deg, rgba(6,6,6,0) 0%, rgba(6,6,6,0) 42%, rgba(6,6,6,0.85) 72%, var(--night) 100%),
      radial-gradient(ellipse 60% 45% at 0% 30%, var(--red) 0%, rgba(242,32,60,0) 100%),
      radial-gradient(ellipse 55% 40% at 30% 100%, var(--blue) 0%, rgba(59,44,168,0) 100%),
      linear-gradient(110deg, var(--red) 0%, var(--magenta) 35%, var(--periwinkle) 70%, var(--violet) 100%);
  }
  .outer-frame {
    position: absolute; left: 143px; top: 221px; width: 595px; height: 794px;
    border: 1px solid rgba(255,255,255,0.85);
  }
  .card {
    position: absolute; left: 168px; top: 254px; width: 540px; height: 725px;
    background: var(--paper);
  }
  .edition {
    position: absolute; left: 250px; top: 112px;
    font-family: "Amatic SC", cursive; font-weight: 700;
    font-size: 215px; line-height: 1; color: var(--ink); letter-spacing: -2px;
    -webkit-text-stroke: 9px var(--ink);
  }
  .edition sup {
    font-size: 46px; vertical-align: baseline; position: relative; top: -10px; left: 8px;
    letter-spacing: 1px; -webkit-text-stroke: 2px var(--ink);
  }
  .title {
    position: absolute; left: 234px; top: 320px;
    font-family: "Amatic SC", cursive; font-weight: 700;
    font-size: 90px; line-height: 105px; color: var(--ink); letter-spacing: 2px;
    text-transform: uppercase; -webkit-text-stroke: 2px var(--ink);
  }
  .title span { display: block; }
  .dates {
    position: absolute; left: 266px; top: 708px;
    font-family: "Poiret One", sans-serif; font-size: 32px; color: var(--ink);
  }
  .venues {
    position: absolute; left: 276px; top: 778px;
    font-family: "Poiret One", sans-serif; font-size: 24px; line-height: 35px; color: var(--ink);
  }
  .website {
    position: absolute; left: 0; width: 874px; top: 940px; text-align: center;
    font-family: "Poiret One", sans-serif; font-size: 15px; color: var(--ink); letter-spacing: 0.5px;
  }
</style>
</head>
<body>
<main class="poster">
  <div class="backdrop" role="img" aria-label="Abstract backdrop of flowing red, violet and blue colour fading into black"></div>

  <div class="outer-frame"></div>
  <section class="card"></section>

  <div class="edition">21<sup>ST</sup></div>
  <h1 class="title">
    <span>Golden Reel</span>
    <span>Indie Screen</span>
    <span>Week</span>
  </h1>
  <p class="dates">NOVEMBER 2 - 11, 2018</p>
  <p class="venues">SF EAST BAY<br>SAN FRANCISCO</p>
  <p class="website">WWW.GRISW.EXAMPLE</p>
</main>
</body>
</html>
```